I need an advertisement w/ a logo to be made. We offer smartphone, tablet, and computer repair and we're located on the Bayshore, NY. My idea for the logo would be a picture of the Bayshore with a cracked smartphone on one side and a computer on the other side, but I'm open to other ideas.

On the ad, I also want it to say "WE REPAIR" and "SMARTPHONES - TABLETS - COMPUTERS" below it, as well as towards the bottom our phone number 555-284-0193 and something along the lines of "Located on Maple W. Ridge Rd. in Harborview"

Another thing about our store is that our services are always on sale, so I want the ad to state that repairs are "25-50% off!" or if possible to have the photoshop PSD file included as well to update pricing information as our prices change.

This is going to be a sponsored ad on Snapgrove so it needs to match the resolution requirements of theirs, and also possibly a print out flyer or poster.

Industry/Entity Type

Phone Repair

Requirements
Must have
• Company name - Bayshore Gadget & Laptop Mending Repair
• Phone Number - 555-284-0193
• State that 25-50% off sale
• Located on Maple W. Ridge Rd. in Harborview
• Our slogan exactly: "If it's broke, we fix it. If you're broke, we buy it!"
• State we repair "smartphones - tablets - computers"
• State we buy broken & used phones & computers for cash
• State We sell used phones & computers
Nice to have
• If theres room to fit in the design, a specific price list for certain screen repairs would be nice.

```html
<!DOCTYPE html>
<html lang="en">
<head>
<meta charset="utf-8">
<title>Bayshore Gadget &amp; Laptop Mending Repair – Ad Set</title>
<link rel="stylesheet" href="https://fonts.googleapis.com/css2?family=Montserrat:wght@500;600;700;800;900&display=swap">
<style>
  :root {
    --stage: #b3b3b3;
    --paper: #ffffff;
    --ink: #363b47;
    --sky: #29abe2;
    --cash: #1e9e4a;
    --panel: #f0f0f0;
    --panel-line: #c9c9c9;
  }
  * { box-sizing: border-box; margin: 0; padding: 0; }
  html, body { width: 1200px; height: 1000px; overflow: hidden; }
  body {
    background: var(--stage);
    font-family: "Montserrat", Arial, sans-serif;
    color: var(--ink);
    position: relative;
  }
  .card { position: absolute; background: var(--paper); overflow: hidden; }
  .card--banner { left: 79px; top: 143px; width: 510px; height: 267px; }
  .card--logo { left: 79px; top: 492px; width: 510px; height: 363px; }
  .card--flyer { left: 616px; top: 143px; width: 505px; height: 714px; }

  .brand-name {
    position: absolute;
    color: var(--sky);
    font-weight: 800;
    line-height: 1.08;
    text-transform: uppercase;
  }
  .card--banner .brand-name { left: 26px; top: 30px; width: 200px; font-size: 21px; }
  .card--logo .brand-name { left: 30px; top: 180px; width: 450px; font-size: 40px; text-align: center; line-height: 1.12; }
  .card--flyer .brand-name { left: 30px; top: 40px; width: 215px; font-size: 22px; }

  .slogan {
    position: absolute;
    background: var(--ink);
    color: var(--paper);
    font-weight: 900;
    line-height: 1.08;
    padding: 12px 18px;
  }
  .card--banner .slogan { left: 247px; top: 24px; width: 240px; height: 127px; font-size: 22px; }
  .card--flyer .slogan { left: 263px; top: 38px; width: 242px; height: 133px; font-size: 24px; padding: 13px 18px; }

  .sale { position: absolute; font-weight: 700; line-height: 1.1; }
  .card--banner .sale {
    left: 247px; top: 164px; width: 240px; height: 77px;
    background: var(--sky); color: var(--paper);
    font-size: 28px; text-align: center; padding-top: 5px;
  }
  .card--flyer .sale {
    left: 0; top: 188px; width: 187px; height: 84px;
    background: var(--ink); color: var(--paper);
    font-size: 29px; padding: 9px 0 0 33px;
  }

  .contact { position: absolute; }
  .contact__row { display: flex; align-items: center; gap: 8px; }
  .contact__icon { width: 30px; height: 30px; flex: none; }
  .contact__phone { font-size: 22px; font-weight: 800; }
  .contact__addr { font-size: 15px; font-weight: 700; line-height: 1.1; }
  .card--banner .contact { left: 23px; top: 169px; }
  .card--flyer .contact { left: 279px; top: 191px; }
  .contact__row + .contact__row { margin-top: 8px; margin-left: 19px; }

  .offers { position: absolute; left: 33px; top: 305px; }
  .offer + .offer { margin-top: 26px; }
  .offer__title { font-size: 20px; font-weight: 700; line-height: 1.2; }
  .offer__detail { font-size: 12px; font-weight: 700; color: var(--sky); }
  .offer__cash { display: block; font-size: 18px; font-weight: 800; color: var(--cash); line-height: 1.1; }

  .footer-band {
    position: absolute; left: 0; top: 532px; width: 505px; height: 182px;
    background: var(--ink);
  }
  .social { position: absolute; left: 35px; top: 584px; list-style: none; }
  .social li { display: flex; align-items: center; gap: 10px; color: var(--paper); font-size: 14px; font-weight: 500; height: 22px; }
  .social li + li { margin-top: 10px; }
  .social__mark { width: 22px; height: 22px; background: var(--sky); flex: none; }

  .price-heading { position: absolute; left: 282px; top: 281px; width: 200px; text-align: center; font-size: 21px; font-weight: 700; }
  .price-card {
    position: absolute; left: 282px; top: 314px; width: 201px; height: 259px;
    background: var(--panel); border: 1px solid var(--panel-line);
    padding: 9px 10px; font-size: 10px; color: var(--sky); line-height: 14.2px;
  }
  .price-card__lead { color: var(--ink); font-weight: 700; font-size: 10.5px; margin-bottom: 4px; }
  .price-table { border-collapse: collapse; }
  .price-table td { padding: 0; }
  .price-table td:first-child { width: 97px; }
  .price-card__note { margin-top: 14px; }
  .price-card__call { margin-top: 14px; }
  .price-card__call strong { color: var(--ink); }
</style>
</head>
<body>

<svg width="0" height="0" style="position:absolute" aria-hidden="true">
  <defs>
    <symbol id="icon-phone" viewBox="0 0 30 30">
      <circle cx="15" cy="15" r="15" fill="#29abe2"/>
      <path d="M10 8.5l2.6-.8 1.8 4-1.6 1.3c.8 1.8 2.1 3.2 3.9 4l1.3-1.6 4 1.8-.8 2.6c-.3 1-1.3 1.5-2.3 1.3-4.9-1.1-8.9-5.1-10-10-.2-1 .3-2.3 1.1-2.6z" fill="#fff"/>
    </symbol>
    <symbol id="icon-pin" viewBox="0 0 30 30">
      <circle cx="15" cy="15" r="15" fill="#29abe2"/>
      <path d="M15 6.5c-3.3 0-5.8 2.5-5.8 5.7 0 4.2 5.8 10.8 5.8 10.8s5.8-6.6 5.8-10.8c0-3.2-2.5-5.7-5.8-5.7z" fill="#fff"/>
      <circle cx="15" cy="12.2" r="2.2" fill="#29abe2"/>
    </symbol>
  </defs>
</svg>

<section class="card card--banner">
  <div class="brand-name">Bayshore Gadget &amp; Laptop Mending Repair</div>
  <div class="slogan">If it's broke,<br>we fix it.<br>If you're broke,<br>we buy it!</div>
  <div class="contact">
    <div class="contact__row">
      <svg class="contact__icon"><use href="#icon-phone"/></svg>
      <span class="contact__phone">555-284-0193</span>
    </div>
    <div class="contact__row">
      <svg class="contact__icon"><use href="#icon-pin"/></svg>
      <span class="contact__addr">Maple W. Ridge Rd.<br>in Harborview</span>
    </div>
  </div>
  <div class="sale">off sale<br>25-50%</div>
</section>

<section class="card card--logo">
  <div class="brand-name">Bayshore Gadget &amp; Laptop Mending Repair</div>
</section>

<section class="card card--flyer">
  <div class="brand-name">Bayshore Gadget &amp; Laptop Mending Repair</div>
  <div class="slogan">If it's broke,<br>we fix it.<br>If you're broke,<br>we buy it!</div>
  <div class="sale">off sale<br>25-50%</div>
  <div class="contact">
    <div class="contact__row">
      <svg class="contact__icon"><use href="#icon-phone"/></svg>
      <span class="contact__phone">555-284-0193</span>
    </div>
    <div class="contact__row">
      <svg class="contact__icon"><use href="#icon-pin"/></svg>
      <span class="contact__addr">Maple W. Ridge Rd.<br>in Harborview</span>
    </div>
  </div>

  <div class="offers">
    <div class="offer">
      <div class="offer__title">We repair</div>
      <div class="offer__detail">smartphones - tablets - computers</div>
    </div>
    <div class="offer">
      <div class="offer__title">We buy</div>
      <div class="offer__detail">broken &amp; used phones &amp; computers<span class="offer__cash">for cash</span></div>
    </div>
    <div class="offer">
      <div class="offer__title">We sell</div>
      <div class="offer__detail">used phones &amp; computers</div>
    </div>
  </div>

  <div class="footer-band"></div>
  <ul class="social">
    <li><span class="social__mark"></span>friendwall.com/yourname</li>
    <li><span class="social__mark"></span>friendwall.com/yourname</li>
    <li><span class="social__mark"></span>friendwall.com/yourname</li>
  </ul>

  <h2 class="price-heading">Price List</h2>
  <div class="price-card">
    <div class="price-card__lead">Cheapest price in the Bayshore!</div>
    <table class="price-table">
      <tr><td>Fonix A1/A2/A3</td><td>$49.99</td></tr>
      <tr><td>Fonix B1</td><td>$59.99*</td></tr>
      <tr><td>Fonix B1 Max</td><td>$64.99*</td></tr>
      <tr><td>Fonix B2</td><td>$99.99*</td></tr>
      <tr><td>Fonix B2 Max</td><td>$109.99*</td></tr>
      <tr><td>Fonix C1</td><td>$199.99*</td></tr>
      <tr><td>Fonix C1 Max</td><td>$249.99*</td></tr>
      <tr><td>Tablo Slim 1,2,3</td><td>$59.99</td></tr>
      <tr><td>Tablo Core 2,3,4</td><td>$49.99</td></tr>
      <tr><td>Tablo Lite 1</td><td>$64.99</td></tr>
    </table>
    <div class="price-card__note">*Price only valid with good LCD.</div>
    <div class="price-card__call">Call today and ask about our FREE computer tune up! <strong>(555) 284-0193</strong></div>
  </div>
</section>

</body>
</html>
```